PEANUT BUTTER DOUGH BOX

I need a box to match our label, Ive provided the box template.
if you need the cmky color pleaas let me know, I can request it.
The Lofty Hours medal art will be best applied to the side of the box
here's the text to copy /paste
DIRECTIONS FOR USE : THC TOLERANCE MAY VARY FROM PERSON TO PERSON. THE ACCEPTED RECOMMENDATION FOR A NEW USER IS 10 MG THC. REFERENCE THE AFFIXED TRAQX TAG FOR ACCURATE DOSAGE INFORMATION.
INGREDIENTS : ZuM PEANUT BUTTER (ROASTED PEANUTS, MOLASSES, MONO AND DIGLYCERIDES, FULLY HYDROGENATED OIL (RAPESEED AND SOYBEAN), PURE CANE SUGAR, SWEET CREAM BUTTER (PASTEURIZED CREAM, SALT), THC CANNABIS EXTRACT
ALLERGEN WARNING : CONTAINS PEANUTS . CONTAINS MILK . CONTAINS SOY .
THE ACTUAL VALUE OF REPORTED CANNABINOIDS MAY VARY FROM THE REPORTED VALUE BY +/-10 %
ACTIVATION TIME :10-60 MIN
WARNING : FOR USE BY INDIVIDUALS 21 YRS OF AGE OR OLDER OR BY REGISTERED QUALIFYING PATIENTS ONLY. IT IS ILLEGAL TO DRIVE A MOTOR VEHICLE WHILE UNDER THE INFLUENCE OF MARIJUANA.
KEEP OUT OF REACH OF CHILDREN.
FEDERAL TOXIN RESPONSE BUREAU
18005937461
WARNING : USE BY PREGNANT OR BREASTFEEDING WOMEN OR BY WOMEN WHO PLAN TO BECOME
PREGNANT MAY RESULT IN FETAL INJURY, PRETERM BIRTH, LOW BIRTHWEIGHT, OR DEVELOPMENTAL
PROBLEMS FOR THE CHILD.
MADE IN A MARIJUANA FACILITY
DISTRIBUTED BY WINIFRED'S HAZE Co.
7382 BRAMBLEWOOD RD, FERNCASTLE MI 49912
LICENSE # KX T 004817
www.HAZEMUFFINS.INFO

```html
<!DOCTYPE html>
<html lang="en">
<head>
<meta charset="utf-8">
<title>Peanut Butter Spread Box – Dieline</title>
<link rel="stylesheet" href="https://fonts.googleapis.com/css2?family=League+Spartan:wght@800&family=Libre+Caslon+Text:wght@700&family=Montserrat:wght@500;700&display=swap">
<style>
  :root {
    --backdrop: #d3e3e8;
    --board: #f6c863;
    --cut-line: #e0338f;
    --fold-line: #d9508f;
    --crimson: #c8304e;
    --gold: #c2a36a;
    --ink: #4a3218;
    --seal-green: #1f8a4c;
    --medal: #b8b8b8;
  }
  html, body {
    margin: 0;
    width: 1200px;
    height: 636px;
    overflow: hidden;
    background: var(--backdrop);
  }
  .canvas {
    width: 1200px;
    height: 636px;
    display: flex;
    align-items: center;
    justify-content: center;
  }
  .dieline { width: 402px; height: 610px; display: block; }
  .board { fill: var(--board); }
  .cut { fill: none; stroke: var(--cut-line); stroke-width: 2; }
  .fold { fill: none; stroke: var(--fold-line); stroke-width: 1.4; stroke-dasharray: 6 5; }
  .slot { stroke: #222; stroke-width: 2.5; }
  .hinge { fill: none; stroke: #3d3d3d; stroke-width: 1; }
  .frame { fill: none; stroke: url(#goldSheen); stroke-width: 5; }
  .tag-frame { fill: none; stroke: var(--gold); stroke-width: 1.2; }
  .brand-name { font-family: "League Spartan", sans-serif; font-weight: 800; fill: var(--crimson); }
  .tagline { font-family: "Libre Caslon Text", serif; font-weight: 700; fill: var(--ink); letter-spacing: 0.6px; }
  .potency { font-family: "League Spartan", sans-serif; font-weight: 800; fill: var(--crimson); letter-spacing: 1px; }
  .fine { font-family: "Montserrat", sans-serif; font-weight: 500; fill: var(--ink); font-size: 6.2px; }
  .fine-bold { font-family: "Montserrat", sans-serif; font-weight: 700; fill: var(--ink); }
  .compliance-mark { fill: #fff; stroke: var(--seal-green); stroke-width: 3; }
  .award-medal { fill: var(--medal); stroke: #7a7a7a; stroke-width: 2; }
  .warning-box { fill: none; stroke: var(--ink); stroke-width: 1; }
</style>
</head>
<body>
<main class="canvas">
  <svg class="dieline" viewBox="300 140 746 1132" xmlns="http://www.w3.org/2000/svg" aria-label="Peanut butter spread box dieline">
    <defs>
      <linearGradient id="goldSheen" x1="0" y1="0" x2="1" y2="1">
        <stop offset="0" stop-color="#a98c55"/>
        <stop offset="0.5" stop-color="#e6d3a3"/>
        <stop offset="1" stop-color="#a98c55"/>
      </linearGradient>
    </defs>

    <!-- board outline -->
    <polygon class="board" points="350,147 995,147 1033,185 1033,285 1020,292 1033,298 1033,675 1020,682 1033,690 1033,790 1015,795 1015,1115 980,1150 918,1150 918,1265 455,1265 455,1150 395,1150 358,1115 358,795 313,790 313,690 326,682 313,675 313,298 326,292 313,285 313,185"/>
    <polygon class="cut" points="350,147 995,147 1033,185 1033,285 1020,292 1033,298 1033,675 1020,682 1033,690 1033,790 1015,795 1015,1115 980,1150 918,1150 918,1265 455,1265 455,1150 395,1150 358,1115 358,795 313,790 313,690 326,682 313,675 313,298 326,292 313,285 313,185"/>

    <!-- inner cut lines -->
    <g class="cuts">
      <path class="cut" d="M483,177 H354 L341,190 V265 L352,280 H405 V242 L483,315"/>
      <path class="cut" d="M890,177 H1019 L1005,190 V265 L994,280 H968 V242 L890,315"/>
      <path class="cut" d="M483,315 H341 V650 H483"/>
      <path class="cut" d="M890,315 H1005 V650 H890"/>
      <path class="cut" d="M483,655 L408,725 V695 H352 L341,708 V760 L354,775 H483"/>
      <path class="cut" d="M890,655 L965,725 V695 H994 L1005,708 V760 L992,775 H890"/>
      <path class="cut" d="M483,797 H382 L366,812 V1118 L392,1140 H483"/>
      <path class="cut" d="M890,797 H991 L1007,812 V1118 L981,1140 H890"/>
    </g>

    <!-- fold lines -->
    <g class="folds">
      <line class="fold" x1="483" y1="147" x2="483" y2="655"/>
      <line class="fold" x1="890" y1="147" x2="890" y2="655"/>
      <line class="fold" x1="483" y1="315" x2="890" y2="315"/>
      <line class="fold" x1="483" y1="795" x2="483" y2="1150"/>
      <line class="fold" x1="890" y1="795" x2="890" y2="1150"/>
      <line class="fold" x1="483" y1="795" x2="890" y2="795"/>
      <line class="fold" x1="455" y1="1150" x2="918" y2="1150"/>
      <rect class="hinge" x="483" y="655" width="407" height="140"/>
    </g>

    <!-- locking slots -->
    <line class="slot" x1="410" y1="380" x2="410" y2="590"/>
    <line class="slot" x1="962" y1="380" x2="962" y2="590"/>

    <!-- back flap: facility and distributor (upside down) -->
    <g class="distributor" transform="rotate(180 686 725)">
      <text class="fine-bold" x="686" y="706" font-size="10.5" text-anchor="middle" letter-spacing="0.6">MADE IN A MARIJUANA FACILITY</text>
      <text class="fine" x="686" y="747" text-anchor="middle">DISTRIBUTED BY WINIFRED'S HAZE Co.</text>
      <text class="fine" x="686" y="758" text-anchor="middle">7382 BRAMBLEWOOD RD, FERNCASTLE MI 49912</text>
      <text class="fine" x="686" y="769" text-anchor="middle">LICENSE # KX T 004817</text>
      <text class="fine" x="686" y="781" text-anchor="middle">www.HAZEMUFFINS.INFO</text>
    </g>

    <!-- front panel -->
    <g class="front-panel">
      <rect class="frame" x="501" y="811" width="373" height="298" rx="26"/>
      <rect class="compliance-mark" x="796" y="848" width="36" height="36" aria-label="Product compliance mark"/>
      <text class="brand-name" x="686" y="975" font-size="66" text-anchor="middle" letter-spacing="1">NUTLARK</text>
      <rect class="tag-frame" x="548" y="1004" width="276" height="42"/>
      <text class="tagline" x="686" y="1022" font-size="11.5" text-anchor="middle">SWEET CREAMED PEANUT BUTTER</text>
      <text class="tagline" x="686" y="1038" font-size="11.5" text-anchor="middle">INFUSED WITH CANNABIS</text>
      <text class="potency" x="686" y="1079" font-size="23" text-anchor="middle">200 MG</text>
    </g>

    <!-- left side panel: award and warnings -->
    <g class="side-left">
      <circle class="award-medal" cx="410" cy="853" r="28" role="img" aria-label="Award medal"/>
      <g transform="translate(466,1012) rotate(90)">
        <text class="fine" text-anchor="middle">
          <tspan x="0" y="0">ACTIVATION TIME :10-60 MIN</tspan>
          <tspan x="0" y="14">WARNING : FOR USE BY INDIVIDUALS 21 YRS OF AGE OR OLDER</tspan>
          <tspan x="0" y="21.5">OR BY REGISTERED QUALIFYING PATIENTS ONLY. IT IS ILLEGAL</tspan>
          <tspan x="0" y="29">TO DRIVE A MOTOR VEHICLE WHILE UNDER THE INFLUENCE OF</tspan>
          <tspan x="0" y="36.5">MARIJUANA.</tspan>
          <tspan x="0" y="44">KEEP OUT OF REACH OF CHILDREN.</tspan>
          <tspan x="0" y="51.5">FEDERAL TOXIN RESPONSE BUREAU</tspan>
          <tspan x="0" y="59">18005937461</tspan>
        </text>
      </g>
      <rect class="warning-box" x="375" y="914" width="32" height="212" rx="4"/>
      <g transform="translate(400,1020) rotate(90)">
        <text class="fine" text-anchor="middle" font-size="5.6">
          <tspan x="0" y="0">WARNING : USE BY PREGNANT OR BREASTFEEDING WOMEN OR</tspan>
          <tspan x="0" y="6.8">BY WOMEN WHO PLAN TO BECOME PREGNANT MAY RESULT IN</tspan>
          <tspan x="0" y="13.6">FETAL INJURY, PRETERM BIRTH, LOW BIRTHWEIGHT, OR</tspan>
          <tspan x="0" y="20.4">DEVELOPMENTAL PROBLEMS FOR THE CHILD.</tspan>
        </text>
      </g>
    </g>

    <!-- right side panel: directions and ingredients -->
    <g class="side-right" transform="translate(910,975) rotate(-90)">
      <text class="fine" text-anchor="middle" font-size="5.6">
        <tspan x="0" y="0">DIRECTIONS FOR USE : THC TOLERANCE MAY VARY FROM PERSON TO PERSON. THE ACCEPTED</tspan>
        <tspan x="0" y="7">RECOMMENDATION FOR A NEW USER IS 10 MG THC. REFERENCE THE AFFIXED TRAQX TAG</tspan>
        <tspan x="0" y="14">FOR ACCURATE DOSAGE INFORMATION.</tspan>
        <tspan x="0" y="24">INGREDIENTS : ZuM PEANUT BUTTER (ROASTED PEANUTS, MOLASSES, MONO AND DIGLYCERIDES,</tspan>
        <tspan x="0" y="31">FULLY HYDROGENATED OIL (RAPESEED AND SOYBEAN), PURE CANE SUGAR,</tspan>
        <tspan x="0" y="38">SWEET CREAM BUTTER (PASTEURIZED CREAM, SALT), THC CANNABIS EXTRACT</tspan>
        <tspan x="0" y="48">ALLERGEN WARNING :</tspan>
        <tspan x="0" y="55">CONTAINS PEANUTS . CONTAINS MILK . CONTAINS SOY .</tspan>
        <tspan x="0" y="65">THE ACTUAL VALUE OF REPORTED CANNABINOIDS MAY VARY</tspan>
        <tspan x="0" y="72">FROM THE REPORTED VALUE BY +/-10 %</tspan>
      </text>
    </g>

    <!-- bottom tuck tab -->
    <g class="tuck-tab">
      <text class="brand-name" x="672" y="1203" font-size="28" text-anchor="middle" letter-spacing="0.5">NUTLARK</text>
      <rect class="compliance-mark" x="742" y="1180" width="20" height="20" stroke-width="2" aria-label="Product compliance mark"/>
    </g>
  </svg>
</main>
</body>
</html>
```